Beer bottle label / Tap badge

What: Graphics to be used on both a beer tap badge and a beer bottle label
Requirements:
• Represent a differentiated quality product
• Include brewery name and logo for brand recognition
• Include and represent the Name “Idle Harbor”
• Include the beer style “American Cream Ale”
• A format that can be used both in a circular tap badge and a square / rectangular bottle label
At Merry Anchor Brewing Co. we design and brew quality beers across a range of styles. We use traditional ingredients and techniques to produce brews for you that are bursting with flavor and easy to drink. Our passion and commitment to excellence are captured in every bottle. Give them a try and see what we mean.
Idle Harbor
American Cream Ale
An easy drinking session beer that won’t make you work to enjoy it. This is crafted to be smooth with a modicum of honey toasted oats and a yeast strain that leaves a fruity, very light, soft balanced palate. Perfectly hopped for a balanced experience this beer is made for you.
Updates
Thanks to everyone who submitted a design. My apologies for not providing any feedback over the past few days since we took a short break over Christmas. We've extended the deadline by a few days and we'll be in touch shortly.
Industry/Entity Type
Brewery
Requirements
Must have
- - Include brewery name and logo for brand recognition
- Include and represent the Name “Idle Harbor”
- Include the beer style “American Cream Ale”
- include volume (330ml) and % alcohol (4.5% alcohol)
Nice to have
- Idle Harbor is a very drinkable, smooth and easy beer that is perfect for a sunny lazy afternoon. We would like the graphic to represent the beer. So, perhaps a friendly (smiling) skeleton on a hammock or on the beach enjoying life .....

```html
<!DOCTYPE html>
<html lang="en">
<head>
<meta charset="utf-8">
<title>Idle Harbor – American Cream Ale Label</title>
<link rel="stylesheet" href="https://fonts.googleapis.com/css2?family=Rye&family=Vollkorn:wght@700&family=Open+Sans:wght@400&display=swap">
<style>
  :root {
    --paper: #ffffff;
    --label-tan: #d3aa8e;
    --maroon: #7a1526;
    --wine: #6b0f20;
    --ink: #111111;
    --ribbon-light: #c99d5c;
    --ribbon-dark: #a5733c;
    --ribbon-tail: #b38650;
    --sun-light: #e6c89e;
    --sun-dark: #c7966c;
    --art-tone: #a7825c;
    --wheat: #8b2434;
    --badge-face: #ffffff;
    --title-glow: #eab9a6;
  }
  html, body {
    margin: 0;
    padding: 0;
    width: 1200px;
    height: 1025px;
    overflow: hidden;
    background: var(--paper);
  }
  .label {
    display: block;
    width: 1200px;
    height: 1025px;
  }
  .brand-name {
    font-family: "Rye", serif;
    fill: var(--ink);
  }
  .beer-name {
    font-family: "Vollkorn", serif;
    font-weight: 700;
    font-size: 112px;
  }
  .beer-name-glow { fill: var(--title-glow); }
  .beer-name-main { fill: var(--wine); }
  .spec {
    font-family: "Open Sans", sans-serif;
    font-size: 27px;
    fill: var(--ink);
  }
  .style-name {
    font-family: "Rye", serif;
    font-size: 36px;
    fill: var(--wine);
  }
</style>
</head>
<body>
<svg class="label" viewBox="0 0 1440 1230" xmlns="http://www.w3.org/2000/svg">
  <defs>
    <radialGradient id="sunburst-tone" cx="50%" cy="40%" r="60%">
      <stop offset="0%" stop-color="var(--sun-light)"/>
      <stop offset="100%" stop-color="var(--sun-dark)"/>
    </radialGradient>
    <linearGradient id="ribbon-tone" x1="0" y1="0" x2="1" y2="0">
      <stop offset="0%" stop-color="var(--ribbon-dark)"/>
      <stop offset="55%" stop-color="var(--ribbon-dark)"/>
      <stop offset="100%" stop-color="var(--ribbon-light)"/>
    </linearGradient>
    <path id="style-arc" d="M511,1007 A355,515 0 0,0 971,1007"/>
  </defs>

  <!-- label frame -->
  <g class="frame">
    <ellipse cx="741" cy="615" rx="447" ry="610" fill="var(--label-tan)" stroke="var(--maroon)" stroke-width="8"/>
    <ellipse cx="741" cy="615" rx="429" ry="592" fill="none" stroke="var(--maroon)" stroke-width="3"/>
    <ellipse cx="741" cy="615" rx="420" ry="583" fill="none" stroke="var(--maroon)" stroke-width="2"/>
    <ellipse cx="741" cy="615" rx="395" ry="553" fill="none" stroke="var(--maroon)" stroke-width="12" stroke-dasharray="3 6"/>
    <ellipse cx="741" cy="615" rx="378" ry="535" fill="none" stroke="var(--maroon)" stroke-width="2"/>
  </g>

  <!-- sunburst backdrop -->
  <ellipse class="sunburst" role="img" aria-label="Sunburst rays backdrop" cx="745" cy="610" rx="335" ry="480" fill="url(#sunburst-tone)"/>

  <!-- mascot illustration area -->
  <rect class="mascot-art" role="img" aria-label="Three smiling skull illustrations" x="575" y="180" width="345" height="128" rx="60" fill="var(--art-tone)"/>

  <!-- brewery name -->
  <g class="brewery">
    <text class="brand-name" x="745" y="420" font-size="82" text-anchor="middle">Merry</text>
    <text class="brand-name" x="745" y="540" font-size="92" text-anchor="middle">Anchor</text>
    <text class="brand-name" x="740" y="625" font-size="60" text-anchor="middle">Brewing Co.</text>
  </g>

  <!-- name ribbon -->
  <g class="ribbon">
    <path d="M300,700 L372,690 L410,885 L305,885 L338,795 Z" fill="var(--ribbon-tail)"/>
    <path d="M1180,705 L1110,700 L1070,885 L1178,885 L1148,795 Z" fill="var(--ribbon-tail)"/>
    <path d="M358,680 Q740,620 1120,705 L1125,865 Q740,795 360,855 Z" fill="url(#ribbon-tone)"/>
    <g transform="rotate(4 740 780)">
      <text class="beer-name beer-name-glow" x="744" y="814" text-anchor="middle">Idle Harbor</text>
      <text class="beer-name beer-name-main" x="740" y="810" text-anchor="middle">Idle Harbor</text>
    </g>
  </g>

  <!-- specs -->
  <text class="spec" x="583" y="874" text-anchor="middle">volume (330ml)</text>
  <text class="spec" x="918" y="872" text-anchor="middle">(4.5% alcohol)</text>

  <!-- wheat and emblem -->
  <ellipse class="wheat" role="img" aria-label="Wheat ear decoration" cx="585" cy="965" rx="30" ry="85" transform="rotate(-40 585 965)" fill="var(--wheat)"/>
  <ellipse class="wheat" role="img" aria-label="Wheat ear decoration" cx="915" cy="965" rx="30" ry="85" transform="rotate(40 915 965)" fill="var(--wheat)"/>
  <circle class="emblem" role="img" aria-label="Emblem of three bottles with stars" cx="748" cy="985" r="100" fill="var(--badge-face)" stroke="var(--maroon)" stroke-width="8" stroke-dasharray="4 3"/>

  <!-- beer style -->
  <text class="style-name">
    <textPath href="#style-arc" startOffset="50%" text-anchor="middle">American Cream Ale</textPath>
  </text>
</svg>
</body>
</html>
```